Business card

We need a business card design for our company based in Auckland , New Zealand called 'Kestrel + Design Ltd'. We provide architectural services. We would like to see designs that use the max. three colours (such as white, black, grey) The final design should communicate financial safety and growth."
Also I will provide our company logo. I would like to the logo to be embeded onto our business card.

Target Market(s)

new residential house, alteration & addition & light commericila design & drafting service

Industry/Entity Type

Architecture

Contact Information for Business Card

Company name: kestrel + design Ltd.
Name: Mark Telford
Job title: architectural designer & Design RQC
email address: mark@kdstudio.co.nz
mobile number: 02 5319 6620
web site: www.kdstudio.co.nz

Requirements
Must have
• My project must have..
• - embeded logo (attached company logo)
• I don't have a bigger version for our company logo, but I have one old one, so you can remove the word from it)
• - insert the attached small PDGQ logo & RQC logo
• - creative, simple and clear business card.
• - Max. three colours
Nice to have
• - Here are the samples I would like to share with you: http://www.velmorindex.com/blog/minimalistic-business-card-designs/
• I would like to have my business card like one of the creation.
Should not have
• TBA

```html
<!DOCTYPE html>
<html lang="en">
<head>
<meta charset="utf-8">
<title>Kestrel + Design Ltd — Business Card</title>
<link href="https://fonts.googleapis.com/css2?family=Open+Sans:wght@400;600&display=swap" rel="stylesheet">
<style>
  :root {
    --page: #ffffff;
    --card-light: #ffffff;
    --card-dark: #0b0b0b;
    --ink: #1a1a1a;
    --ink-light: #ffffff;
    --grey: #8a8d8a;
    --rule-light: #d6d6d6;
    --rule-dark: #3a3a3a;
  }
  * { box-sizing: border-box; margin: 0; padding: 0; }
  html, body {
    width: 1200px; height: 1200px; overflow: hidden;
    background: var(--page);
    font-family: "Open Sans", Arial, sans-serif;
  }
  .canvas { position: relative; width: 1200px; height: 1200px; }

  .card { position: absolute; box-shadow: 3px 4px 8px rgba(0,0,0,0.35); }

  /* Front */
  .card-front {
    left: 178px; top: 57px; width: 854px; height: 509px;
    background: var(--card-light);
    border: 1px solid #e2e2e2;
  }
  .brand-mark { position: absolute; left: 123px; top: 139px; }
  .front-divider {
    position: absolute; left: 367px; top: 140px;
    width: 2px; height: 177px; background: var(--rule-light);
  }
  .company-name {
    position: absolute; left: 410px; top: 160px;
    font-size: 38px; font-weight: 600; line-height: 49px;
    color: var(--ink);
  }

  /* Back */
  .card-back {
    left: 183px; top: 631px; width: 835px; height: 500px;
    background: var(--card-dark);
  }
  .member-badge {
    position: absolute; left: 78px; top: 55px;
    width: 176px; height: 68px; background: var(--grey);
  }
  .member-label {
    position: absolute; left: 119px; top: 135px;
    font-size: 21px; font-weight: 600; line-height: 25px;
    color: var(--grey);
  }
  .practitioner-badge {
    position: absolute; left: 77px; top: 294px;
    width: 138px; height: 138px; border-radius: 50%;
    background: var(--ink-light);
  }
  .back-divider {
    position: absolute; left: 367px; top: 171px;
    width: 2px; height: 151px; background: var(--rule-dark);
  }
  .contact { position: absolute; left: 429px; top: 166px; color: var(--ink-light); }
  .person-name { font-size: 27px; font-weight: 400; line-height: 34px; }
  .person-title { font-size: 18px; line-height: 24px; margin-top: 2px; }
  .contact-list { list-style: none; margin-top: 26px; font-size: 17px; line-height: 26.5px; }
  .contact-list li { display: flex; }
  .contact-key { width: 117px; }
</style>
</head>
<body>
<main class="canvas">
  <section class="card card-front" aria-label="Business card front">
    <svg class="brand-mark" width="180" height="180" viewBox="0 0 180 180" aria-hidden="true">
      <circle cx="90" cy="90" r="84" fill="none" stroke="var(--ink)" stroke-width="8"/>
    </svg>
    <div class="front-divider"></div>
    <h1 class="company-name">Kestrel +<br>Design Ltd</h1>
  </section>

  <section class="card card-back" aria-label="Business card back">
    <div class="member-badge" aria-hidden="true"></div>
    <p class="member-label">Professional<br>Member</p>
    <div class="practitioner-badge" aria-hidden="true"></div>
    <div class="back-divider"></div>
    <div class="contact">
      <p class="person-name">Mark Telford</p>
      <p class="person-title">Architectural Designer &amp; Design RQC</p>
      <ul class="contact-list">
        <li><span class="contact-key">T</span><span>02 5319 6620</span></li>
        <li><span class="contact-key">M</span><span>mark@kdstudio.co.nz</span></li>
        <li><span class="contact-key">W</span><span>www.kdstudio.co.nz</span></li>
      </ul>
    </div>
  </section>
</main>
</body>
</html>
```